Blind Rivet Product catalogue

Need a design in wordpress with a productcatalogue where i present all products. This is a B2B business. The products is Blindrivets and Blindrivet nuts and accessories to this. I only want the basic information and also technical specification.

This is a subcompany to my existing company k7.m9.se but specializing in a subcategory

Target Market(s)

Businesses using blind rivet technology.

Industry/Entity Type

Industrial

Coding

Coded - Design and coding required

Number of Pages Required

5+ page

Font styles to use
Sans Serif

Requirements
Must have
• Three different categories for the products; Blind Rivets - Blind Rivet Nut - Riveting Tools
Nice to have
• Possible to ad login for more information of the different sizes

```html
<!DOCTYPE html>
<html lang="en">
<head>
<meta charset="utf-8">
<title>k7.m9.se – Blind Riveting Products</title>
<link rel="stylesheet" href="https://fonts.googleapis.com/css2?family=Montserrat:wght@400;500;600;700&display=swap">
<style>
:root{
  --orange:#ff6a13;
  --ink:#2d2d2d;
  --muted:#7a7a7a;
  --light:#f4f4f4;
  --white:#ffffff;
  --cta-dark:#3b3b3b;
  --footer:#2a2a2a;
  --footer-line:#3c3c3c;
  --footer-text:#b9b9b9;
}
*{box-sizing:border-box;margin:0;padding:0}
html,body{width:1200px;height:2204px;overflow:hidden}
body{font-family:"Montserrat",Arial,sans-serif;color:var(--ink);background:var(--white)}
.page{width:1200px;height:2204px;display:flex;flex-direction:column}

/* header */
.site-header{height:100px;display:flex;align-items:center;justify-content:space-between;padding:0 90px;border-bottom:1px solid #eee}
.brand{font-size:34px;font-weight:500;color:var(--ink);letter-spacing:1px}
.main-nav{display:flex;align-items:center;gap:36px;font-size:14px;font-weight:500}
.btn{display:inline-block;background:var(--orange);color:var(--white);font-weight:600;font-size:13px;padding:12px 28px;border-radius:2px}

/* hero */
.hero{height:640px;display:flex;align-items:center;padding:0 90px;gap:70px;position:relative}
.hero-visual{width:480px;height:400px;border-radius:6px;background:radial-gradient(circle at 50% 50%,#f5a44c 0%,#e07d1f 35%,#3a3a3a 70%,#f4f4f4 72%)}
.hero-copy{flex:1}
.hero-title{font-size:50px;font-weight:700;line-height:1.15;margin-bottom:22px}
.accent{color:var(--orange)}
.hero-text{font-size:15px;line-height:1.7;color:var(--muted);margin-bottom:30px;max-width:470px}
.contact-row{display:flex;align-items:center;gap:14px;font-size:15px;margin-bottom:16px}
.contact-icon{width:36px;height:36px;border-radius:50%;background:#ffe6d6;display:flex;align-items:center;justify-content:center}
.slider-dots{position:absolute;bottom:34px;left:0;right:0;display:flex;justify-content:center;gap:10px}
.slider-dots span{width:10px;height:10px;border-radius:50%;background:#d6d6d6}
.slider-dots span.active{background:var(--orange)}

/* products */
.products{height:760px;background:var(--light);padding:70px 90px 0;text-align:center}
.section-title{font-size:36px;font-weight:700;margin-bottom:16px}
.section-intro{font-size:15px;line-height:1.7;color:var(--muted);max-width:640px;margin:0 auto 50px}
.product-grid{display:flex;gap:40px}
.product-card{flex:1;background:var(--white);padding:30px 26px 34px;border-radius:4px}
.product-image{height:260px;border-radius:4px;margin-bottom:24px;background:linear-gradient(160deg,#fafafa,#d9d9d9)}
.product-image.tool{background:linear-gradient(160deg,#fafafa,#cfcfcf 60%,#3a3a3a)}
.product-name{font-size:19px;font-weight:700;margin-bottom:10px}
.product-text{font-size:14px;line-height:1.6;color:var(--muted);margin-bottom:22px}

/* call to action */
.cta{height:220px;display:flex}
.cta-panel{flex:1;display:flex;flex-direction:column;justify-content:center;padding:0 90px}
.cta-panel.stock{background:var(--cta-dark);color:var(--white)}
.cta-panel.request{background:var(--orange);color:var(--white)}
.cta-title{font-size:30px;font-weight:700;margin-bottom:12px}
.cta-link{font-size:14px;font-weight:500;display:flex;align-items:center;gap:10px}

/* footer */
.site-footer{flex:1;background:var(--footer);color:var(--footer-text);display:flex;flex-direction:column}
.footer-columns{flex:1;display:flex;gap:60px;padding:70px 90px 0}
.footer-col{flex:1}
.footer-col.newsletter{flex:1.3}
.footer-heading{color:var(--white);font-size:18px;font-weight:700;margin-bottom:26px}
.footer-item{display:flex;align-items:flex-start;gap:12px;font-size:14px;line-height:1.6;margin-bottom:16px}
.social{display:flex;gap:12px;margin-top:24px}
.social span{width:34px;height:34px;border-radius:50%;background:var(--orange)}
.link-list{list-style:none;font-size:14px}
.link-list li{margin-bottom:16px}
.newsletter-text{font-size:14px;line-height:1.6;margin-bottom:22px}
.field{height:48px;border:1px solid #555;background:#333;color:#888;font-size:14px;display:flex;align-items:center;padding:0 16px;margin-bottom:14px}
.footer-bottom{height:70px;border-top:1px solid var(--footer-line);display:flex;align-items:center;justify-content:center;font-size:13px}
</style>
</head>
<body>
<div class="page">

  <header class="site-header">
    <div class="brand">k7.m9.se</div>
    <nav class="main-nav">
      <span>Home</span>
      <span>Products</span>
      <span class="btn">Contact Us</span>
    </nav>
  </header>

  <section class="hero">
    <div class="hero-visual" role="img" aria-label="Open black case with orange compartments holding blind rivets"></div>
    <div class="hero-copy">
      <h1 class="hero-title">Lorem Ipsum Is Simply <span class="accent">Dummy Text</span></h1>
      <p class="hero-text">Quality blind rivets, rivet nuts and tools for industrial use, supplied fast with full technical specifications.</p>
      <div class="contact-row">
        <span class="contact-icon"><svg width="16" height="16" viewBox="0 0 24 24"><rect x="2" y="5" width="20" height="14" rx="2" fill="none" stroke="#ff6a13" stroke-width="2"/><path d="M2 7l10 7 10-7" fill="none" stroke="#ff6a13" stroke-width="2"/></svg></span>
        info@k7.m9.se
      </div>
      <div class="contact-row">
        <span class="contact-icon"><svg width="16" height="16" viewBox="0 0 24 24"><path d="M6 2h4l2 5-3 2a12 12 0 006 6l2-3 5 2v4a2 2 0 01-2 2A18 18 0 014 4a2 2 0 012-2z" fill="#ff6a13"/></svg></span>
        +46 00 000 00 00
      </div>
    </div>
    <div class="slider-dots"><span class="active"></span><span></span><span></span></div>
  </section>

  <section class="products">
    <h2 class="section-title">Blind Riveting <span class="accent">Products</span></h2>
    <p class="section-intro">Browse our three categories and find the right fastening solution with basic information and technical data.</p>
    <div class="product-grid">
      <article class="product-card">
        <div class="product-image" role="img" aria-label="Silver blind rivet"></div>
        <h3 class="product-name">Blind Rivets</h3>
        <p class="product-text">Strong fastening for thin sheet materials.</p>
        <span class="btn">Read More</span>
      </article>
      <article class="product-card">
        <div class="product-image" role="img" aria-label="Silver blind rivet nut"></div>
        <h3 class="product-name">Blind Rivet Nuts</h3>
        <p class="product-text">Threaded inserts for durable joints.</p>
        <span class="btn">Read More</span>
      </article>
      <article class="product-card">
        <div class="product-image tool" role="img" aria-label="Cordless riveting tool"></div>
        <h3 class="product-name">Riveting Tools</h3>
        <p class="product-text">Manual and battery tools for daily work.</p>
        <span class="btn">Read More</span>
      </article>
    </div>
  </section>

  <section class="cta">
    <div class="cta-panel stock">
      <h2 class="cta-title">Check Our Actual Stock</h2>
      <span class="cta-link">View stock <svg width="18" height="12" viewBox="0 0 18 12"><path d="M0 6h16M11 1l5 5-5 5" fill="none" stroke="#fff" stroke-width="2"/></svg></span>
    </div>
    <div class="cta-panel request">
      <h2 class="cta-title">Make A Request</h2>
      <span class="cta-link">Send request <svg width="18" height="12" viewBox="0 0 18 12"><path d="M0 6h16M11 1l5 5-5 5" fill="none" stroke="#fff" stroke-width="2"/></svg></span>
    </div>
  </section>

  <footer class="site-footer">
    <div class="footer-columns">
      <div class="footer-col">
        <h3 class="footer-heading">Contact Us</h3>
        <div class="footer-item"><svg width="16" height="18" viewBox="0 0 24 24"><path d="M12 2a7 7 0 00-7 7c0 5 7 13 7 13s7-8 7-13a7 7 0 00-7-7zm0 10a3 3 0 110-6 3 3 0 010 6z" fill="#ff6a13"/></svg><span>Industrigatan 1, 000 00 Sample City</span></div>
        <div class="footer-item"><svg width="16" height="16" viewBox="0 0 24 24"><rect x="2" y="5" width="20" height="14" rx="2" fill="none" stroke="#ff6a13" stroke-width="2"/><path d="M2 7l10 7 10-7" fill="none" stroke="#ff6a13" stroke-width="2"/></svg><span>info@k7.m9.se</span></div>
        <div class="footer-item"><svg width="16" height="16" viewBox="0 0 24 24"><path d="M6 2h4l2 5-3 2a12 12 0 006 6l2-3 5 2v4a2 2 0 01-2 2A18 18 0 014 4a2 2 0 012-2z" fill="#ff6a13"/></svg><span>+46 00 000 00 00</span></div>
        <div class="social"><span></span><span></span><span></span></div>
      </div>
      <div class="footer-col">
        <h3 class="footer-heading">Quick Links</h3>
        <ul class="link-list">
          <li>Home</li>
          <li>Blind Rivets</li>
          <li>Blind Rivet Nuts</li>
          <li>Riveting Tools</li>
          <li>Contact</li>
        </ul>
      </div>
      <div class="footer-col newsletter">
        <h3 class="footer-heading">Newsletter Subscription</h3>
        <p class="newsletter-text">Get news about products and offers straight to your inbox.</p>
        <div class="field">Your email</div>
        <span class="btn">Subscribe</span>
      </div>
    </div>
    <div class="footer-bottom">© k7.m9.se All rights reserved</div>
  </footer>

</div>
</body>
</html>
```